Womens Scarves & Accessories Homepage Design

When developing this site design please have a focus on modern, stylish design. A good example of the kind of design style the client really like can be found at www.qorvistyle.com

As fashion products are the focus here clear, appealing presentation of product images is critical.

We are after a combination of http://dev40.kqrtw.com.au/index.php/ mixed in with the brief file attached.

Some hero shot images have been attached

Target Market(s)

Consumer:
Lady 30 - 50
high disposable income
updating wardrobe
enjoys the shopping experience

Industry/Entity Type

Fashion

Requirements
Must have
• premium quality and elegant products - well packaged - boutique and elegant in style

The current logo must not be changed.

The slogan "spoil the girl within" must remain the same and use the current font displayed in http://dev40.kqrtw.com.au

```html
<!DOCTYPE html>
<html lang="en">
<head>
<meta charset="utf-8">
<title>Velle Rosa – Spoil The Girl Within</title>
<link href="https://fonts.googleapis.com/css2?family=Raleway:wght@300;400&family=Open+Sans:wght@400;600;700&display=swap" rel="stylesheet">
<style>
:root{
  --page-bg-top:#f7dfe6;
  --page-bg-bottom:#f4d3dd;
  --pink:#f49ab8;
  --pink-deep:#ec87a9;
  --pink-tile:#f7a9c4;
  --pink-text:#e66a95;
  --nav-bg:#f3f0f1;
  --nav-active:#e9e3d2;
  --panel:#ffffff;
  --sidebar:#eeeeee;
  --label-bar:#e8e0cb;
  --ink:#555555;
  --ink-soft:#888888;
  --white:#ffffff;
}
*{box-sizing:border-box;margin:0;padding:0}
html,body{width:1200px;height:900px;overflow:hidden}
body{
  position:relative;
  font-family:"Open Sans",Arial,sans-serif;
  background:linear-gradient(180deg,var(--page-bg-top),var(--page-bg-bottom));
  color:var(--ink);
}
.abs{position:absolute}

/* header */
.brand{left:84px;top:2px;width:130px;height:92px;border-radius:50%;background:var(--white);border:4px solid #e9e3c8;display:flex;align-items:center;justify-content:center;font-family:"Raleway",sans-serif;font-weight:400;font-size:20px;color:#333}
.slogan{left:216px;top:8px;font-family:"Raleway",sans-serif;font-weight:300;font-size:36px;line-height:40px;color:#6b6b6b}
.toolbar{left:424px;top:0;width:174px;height:22px;background:#f6eef1;border-radius:0 0 8px 8px;font-size:7px;color:#777;display:flex;align-items:center;gap:5px;padding:0 6px}
.flag{width:14px;height:9px;background:#2b3f8c;border:1px solid #c8102e}
.currency{width:46px;height:10px;background:#fff;border:1px solid #bbb;font-size:6px;padding-left:2px;line-height:8px}
.cart-icon{left:426px;top:30px}
.cart-status{left:481px;top:38px;font-size:12px;color:#777}
.btn{top:72px;height:20px;border-radius:10px;background:var(--pink);color:#4a4a4a;font-size:12px;font-weight:600;display:flex;align-items:center;padding-left:24px;white-space:nowrap}
.btn::before{content:"";position:absolute;left:3px;top:2px;width:16px;height:16px;border-radius:50%;background:#fbd3e0}
.btn::after{content:"";position:absolute;left:9px;top:6px;border-left:6px solid #fff;border-top:4px solid transparent;border-bottom:4px solid transparent}
.btn-cart{left:424px;width:86px}
.btn-checkout{left:513px;width:85px}

/* nav */
.nav{left:84px;top:98px;width:514px;height:33px;background:var(--nav-bg);font-family:"Raleway",sans-serif;font-size:10.5px}
.nav a{position:absolute;top:0;height:33px;line-height:33px;text-align:center;color:var(--pink-text);text-decoration:none;border-right:1px solid #e2dbdd;white-space:nowrap}
.nav a.current{background:var(--nav-active);color:#444}
.search{left:492px;top:106px;width:99px;height:18px;border-radius:9px;background:#e6e1e3}
.search svg{position:absolute;right:3px;top:2px}

/* hero */
.hero{left:84px;top:131px;width:514px;height:271px;background:linear-gradient(110deg,#c7383b 0%,#3a2e2c 35%,#b39a8e 55%,#2a2424 75%,#e4dfe0 100%)}

/* category tiles */
.tile{top:402px;width:170px;height:72px;background:var(--pink-tile);color:var(--white);padding:8px 7px}
.tile h2{font-size:12px;font-weight:700;letter-spacing:.2px;margin-bottom:6px;white-space:nowrap}
.tile p{font-size:6.3px;line-height:10px;color:#7a5a64;padding-right:10px}
.tile .go{position:absolute;right:7px;bottom:5px;width:13px;height:13px;border-radius:50%;background:#fbd9e4}
.tile .go::after{content:"";position:absolute;left:5px;top:3.5px;border-left:4px solid #fff;border-top:3px solid transparent;border-bottom:3px solid transparent}

/* catalogue */
.sidebar{left:84px;top:474px;width:100px;height:251px;background:var(--sidebar)}
.sidebar li{list-style:none;height:25px;line-height:25px;padding-left:6px;font-size:7.5px;color:#888;border-bottom:1px solid #fff;white-space:nowrap}
.products{left:184px;top:474px;width:414px;height:251px;background:var(--panel)}
.card{top:486px;width:118px;height:202px;box-shadow:0 1px 2px rgba(0,0,0,.15)}
.card h3{height:21px;background:var(--label-bar);border-radius:4px 4px 0 0;font-family:"Raleway",sans-serif;font-weight:400;font-size:11px;color:#555;line-height:21px;padding-left:6px}
.card .photo{height:181px;background:linear-gradient(180deg,#5a5a5a 0%,#a07a55 40%,#c6438f 75%,#5b5b5b 100%)}

/* footer */
.footer-band{left:0;top:725px;width:1200px;height:127px;background:var(--pink)}
.footer-col{top:725px;height:127px;border-right:1px solid #f9bdd1}
.footer-title{font-family:"Raleway",sans-serif;font-weight:400;font-size:12px;color:#555;white-space:nowrap}
.perk{font-size:9px;color:#fde3ec;left:109px;white-space:nowrap}
.perk b{font-weight:700;color:#fff}
.perk::before{content:"";position:absolute;left:-16px;top:3px;width:10px;height:8px;border-top:2px solid #ec6d97;border-right:2px solid #ec6d97;border-radius:0 6px 0 0}
.quote{left:252px;top:762px;width:158px;font-size:6.2px;line-height:9.5px;color:#fff}
.quote-by{left:252px;top:802px;font-size:6.2px;color:#c97a95;white-space:nowrap}
.pay-card{top:739px;width:30px;height:20px;border-radius:2px}
.pay-note{left:462px;top:771px;font-size:9.5px;color:#555;white-space:nowrap}
.secure{left:490px;top:787px;font-size:10px;color:#555;white-space:nowrap}
.lock{left:467px;top:787px;width:18px;height:13px;background:#d9a437;border-radius:2px}
.badge{left:466px;top:806px;width:107px;height:20px;border-radius:3px;background:#ffffff}
.badge-dot{left:469px;top:809px;width:14px;height:14px;border-radius:50%;background:#f08a3c}
.bottom-bar{left:0;top:852px;width:1200px;height:48px;background:var(--pink-deep)}
.links{left:110px;top:864px;font-size:6.6px;color:#fff;white-space:nowrap}
.copy{left:287px;top:881px;font-size:6.8px;color:#fff;white-space:nowrap}
</style>
</head>
<body>

<header>
  <div class="abs brand">Velle Rosa</div>
  <div class="abs slogan">Spoil The<br>Girl Within</div>
  <div class="abs toolbar">
    <span>language:</span><span class="flag"></span>
    <span style="margin-left:10px">Crruncy:</span><span class="currency">US Dollar</span><span class="flag" style="margin-left:6px"></span>
  </div>
  <svg class="abs cart-icon" width="36" height="32" viewBox="0 0 36 32" aria-hidden="true">
    <path d="M2 4h6l4 16h18l4-12H10" fill="#e23b3b" stroke="#b22" stroke-width="1.5"/>
    <circle cx="14" cy="26" r="3" fill="#666"/><circle cx="27" cy="26" r="3" fill="#666"/>
  </svg>
  <div class="abs cart-status">Your Cart is Empty</div>
  <div class="abs btn btn-cart">Veiw Cart</div>
  <div class="abs btn btn-checkout">Checkout</div>
</header>

<nav class="abs nav">
  <a class="current" style="left:0;width:44px">Home</a>
  <a style="left:44px;width:53px">About us</a>
  <a style="left:97px;width:53px">Products</a>
  <a style="left:150px;width:67px">Special Offer</a>
  <a style="left:217px;width:70px">Testimonials</a>
  <a style="left:287px;width:35px">FAQ</a>
  <a style="left:322px;width:60px;border-right:0">Contact us</a>
</nav>
<div class="abs search">
  <svg width="14" height="14" viewBox="0 0 14 14" aria-hidden="true"><circle cx="7" cy="7" r="6" fill="#bdb7b9"/><circle cx="6.3" cy="6.3" r="2.5" fill="none" stroke="#fff" stroke-width="1.2"/><path d="M8 8l2.5 2.5" stroke="#fff" stroke-width="1.2"/></svg>
</div>

<div class="abs hero" role="img" aria-label="Hero photograph: a woman in sunglasses and a fur wrap seated in a red open-top vintage car"></div>

<section>
  <div class="abs tile" style="left:84px"><h2>SCARVES</h2><p>simply dummy text of the printing and typesetting industry. Lorem Ipsum has been the industry's standard dummy text ever since the.</p><span class="go"></span></div>
  <div class="abs tile" style="left:256px"><h2>WRAPS &amp; SHAWLS</h2><p>simply dummy text of the printing and typesetting industry. Lorem Ipsum has been the industry's standard dummy text ever since the.</p><span class="go"></span></div>
  <div class="abs tile" style="left:428px"><h2>COSTUME JWELERY</h2><p>simply dummy text of the printing and typesetting industry. Lorem Ipsum has been the industry's standard dummy text ever since the.</p><span class="go"></span></div>
</section>

<ul class="abs sidebar">
  <li>SCARVES</li><li>WRAPS &amp; SHAWLS</li><li>COSTUME JWELERY</li><li>GIFTS</li><li>SCCESSORIES</li><li>SPECIALS</li>
</ul>
<div class="abs products"></div>
<div class="abs card" style="left:190px"><h3>Modern Scarf</h3><div class="photo" role="img" aria-label="Product photograph: model wearing a pink checked scarf"></div></div>
<div class="abs card" style="left:330px"><h3>Modern Scarf</h3><div class="photo" role="img" aria-label="Product photograph: model wearing a pink checked scarf"></div></div>
<div class="abs card" style="left:471px"><h3>Modern Scarf</h3><div class="photo" role="img" aria-label="Product photograph: model wearing a pink checked scarf"></div></div>

<footer>
  <div class="abs footer-band"></div>
  <div class="abs footer-col" style="left:84px;width:155px"></div>
  <div class="abs footer-col" style="left:239px;width:184px"></div>
  <h4 class="abs footer-title" style="left:93px;top:735px">Why VelleRosa?</h4>
  <div class="abs perk" style="top:761px"><b>90</b> Days Return Policy</div>
  <div class="abs perk" style="top:781px"><b>Free</b> Shipping Both Ways</div>
  <div class="abs perk" style="top:801px"><b>Loyalty</b> Program</div>
  <h4 class="abs footer-title" style="left:252px;top:735px">Testimonials</h4>
  <p class="abs quote">Lorem ipsum dolor sit amet, consectetur adipiscing elit. Donec euismod arcu a mi fermentum varius.</p>
  <div class="abs quote-by">Ada Lorne - Brookvale</div>
  <div class="abs pay-card" style="left:478px;background:#e8e2d0"></div>
  <div class="abs pay-card" style="left:526px;background:#7fc7e0"></div>
  <div class="abs pay-note">Offline Payments ACCEPTED</div>
  <div class="abs lock"></div>
  <div class="abs secure">Secure Shopping</div>
  <div class="abs badge"></div>
  <div class="abs badge-dot"></div>
  <div class="abs bottom-bar"></div>
  <div class="abs links">BEST SELLERS &nbsp;|&nbsp; SCARVES &nbsp;|&nbsp; WRAPS &amp; SHAWLS &nbsp;|&nbsp; ACCESSORIES &nbsp;|&nbsp; GIFTS &nbsp;|&nbsp; PECIALS &nbsp;|&nbsp; ABOUT US &nbsp;|&nbsp; TESTIMONIALS &nbsp;|&nbsp; FAQ &nbsp;|&nbsp; CONTACT US</div>
  <div class="abs copy">© 2011 Velle Rosa. All Rights reserved</div>
</footer>

</body>
</html>
```